Kellwood Build, Carpentry Services

Business card for carpentry business in the Sunshine Coast.

Business card layout required using logo provided - provided both PDF copy and AI. Please let me know if you would like a the files for the logo symbol and text by itself.

Business Colours are grey, blue and white. The font colours codes for this design are Blue Hex # 00B4E6 and Hex # 39393B for the gray colour.

FYI font for logo is Gotham Bold.

Preference for a clean and striking layout that is simple and elegant.

Target Market(s)

Young Families, retirees, young couples requiring assistance with small to medium works/renovations on the Sunshine Coast.

Industry/Entity Type

Construction

Contact Information for Business Card

Dean Kellwood
Carpenter
0489305627
dean@kellwoodbuild.com.au
Tarrawin Heads, Amber Coast
RHPA Licensed Carpenter (In smaller font)

Font styles to use
Sans Serif

Colors

Designer to choose colors to be used in the design.

Requirements
Must have
• Logo provided must appear on the card, preferably on one side of the card by itself with the text on the alternate side
Nice to have
• Text on the other side of card, maybe grey background and white font here but happy for the designer to provide ideas here.
Should not have
• Use of other colours, other than the ones provided - white, grey and blue. Black optional.

```html
<!DOCTYPE html>
<html lang="en">
<head>
<meta charset="UTF-8">
<title>Kellwood Build – Business Card</title>
<link rel="stylesheet" href="https://fonts.googleapis.com/css2?family=Arimo:wght@400;700&family=Montserrat:wght@700&display=swap">
<style>
  :root {
    --blue: #00B4E6;
    --grey: #39393B;
    --white: #FFFFFF;
    --backdrop: #ECEAE6;
  }
  * { margin: 0; padding: 0; box-sizing: border-box; }
  html, body {
    width: 1200px;
    height: 1200px;
    overflow: hidden;
  }
  body {
    position: relative;
    background: var(--backdrop);
    font-family: "Arimo", Arial, sans-serif;
  }
  .card {
    position: absolute;
    left: 202px;
    width: 796px;
    height: 486px;
    background: linear-gradient(to bottom, var(--blue) 0 50%, var(--grey) 50% 100%);
  }
  .card--front { top: 79px; }
  .card--back { top: 634px; }
  .card__face {
    position: absolute;
    left: 43px;
    top: 43px;
    width: 710px;
    height: 401px;
    background: var(--white);
  }
  .brand {
    position: absolute;
    left: 0;
    right: 0;
    top: 50%;
    transform: translateY(-50%);
    display: flex;
    align-items: center;
    justify-content: center;
    gap: 16px;
  }
  .brand__mark {
    width: 28px;
    height: 28px;
    background: var(--grey);
  }
  .brand__name {
    font-family: "Montserrat", Arial, sans-serif;
    font-weight: 700;
    font-size: 33px;
    letter-spacing: 1.5px;
    color: var(--blue);
    text-transform: uppercase;
  }
  .identity {
    position: absolute;
    left: 0;
    right: 0;
    top: 164px;
    text-align: center;
    color: var(--blue);
  }
  .identity__name {
    font-weight: 700;
    font-size: 44px;
    letter-spacing: 2.4px;
    line-height: 1.05;
    text-transform: uppercase;
  }
  .identity__role {
    font-size: 24px;
    letter-spacing: 1.8px;
    text-transform: uppercase;
    margin-top: 1px;
  }
  .contact {
    position: absolute;
    left: 0;
    right: 0;
    top: 312px;
    text-align: center;
    color: var(--grey);
    font-size: 21px;
    letter-spacing: 0.8px;
    line-height: 23px;
  }
  .contact__licence {
    font-size: 12.5px;
    letter-spacing: 1px;
    text-transform: uppercase;
    margin-top: 5px;
  }
</style>
</head>
<body>
  <section class="card card--front">
    <div class="card__face">
      <div class="brand">
        <span class="brand__mark" aria-hidden="true"></span>
        <span class="brand__name">Kellwood Build</span>
      </div>
    </div>
  </section>

  <section class="card card--back">
    <div class="card__face">
      <div class="identity">
        <h1 class="identity__name">Dean Kellwood</h1>
        <p class="identity__role">Carpenter</p>
      </div>
      <div class="contact">
        <p class="contact__line">0489305627 | dean@kellwoodbuild.com.au</p>
        <p class="contact__line">Tarrawin Heads, Amber Coast</p>
        <p class="contact__licence">RHPA Licensed Carpenter</p>
      </div>
    </div>
  </section>
</body>
</html>
```